Company Brochure and Presentation

Hello,

We are software development company and would like to design our company brochure (Both in high resolution Printable Format and PDF) and presentation (PPT).

The contents are ready for both assignment. Just need to align with creative design.

Please submit your portfolio so that we can short list and send you the contents.

Also, please include cost and time-frame.

Few more details for best quotation...

The company profile will have around 15 pages
The presentation (PPT) will also have 15 pages.

However, I am open for your suggestion to make it more professional designed, include more images and with less pages.

The files are attached herewith.

The rough images/ ideas for outsourcing models are provided in word file. Open for your ideas here.

Please review and let me know your best quote.

Also, please read below link before you quote so you can make a competitive bid.

http://www.pixelbazaar.example/quote-pixelbazaar.aspx?briefid=48203

Thanks & Best Regards,

Ravesh Kotadia
Skype - ravesh.k.kotadia
Updates

Hello All,

I hove uploaded few images like logo, banner etc. You can use those image or take as a reference. 

Also, please visit our website - www.veloquent.example 

Thank you.

Target Market(s)

1. IT Department of the companies
2. Outsourcing IT companies
3. IT consultant

Industry/Entity Type

Software

```html
<!DOCTYPE html>
<html lang="en">
<head>
<meta charset="utf-8">
<title>Vision, Mission &amp; Objective</title>
<link href="https://fonts.googleapis.com/css2?family=Didact+Gothic&display=swap" rel="stylesheet">
<style>
  :root {
    --page-bg: #ffffff;
    --title-grey: #6d6e70;
    --heading-white: #ffffff;
    --body-text: #e6ecd6;
    --rule-yellow: #d9e04a;
    --green-light: #a4bd3c;
    --green-mid: #5f9434;
    --green-dark: #2a6230;
    --band-blue: #1f4f77;
    --band-silver: #c9cdd2;
    --photo-light: #d8d6d2;
    --photo-dark: #3a3c42;
  }
  html, body {
    margin: 0;
    padding: 0;
    width: 919px;
    height: 1200px;
    overflow: hidden;
    background: var(--page-bg);
  }
  .page {
    position: relative;
    width: 919px;
    height: 1200px;
    overflow: hidden;
    font-family: "Didact Gothic", "Century Gothic", sans-serif;
  }
  .backdrop {
    position: absolute;
    inset: 0;
  }
  .page-title {
    position: absolute;
    left: 418px;
    top: 378px;
    margin: 0;
    font-weight: 400;
    font-size: 56px;
    line-height: 72px;
    color: var(--title-grey);
    letter-spacing: 0.5px;
  }
  .statement {
    position: absolute;
    left: 23px;
    width: 872px;
  }
  .statement h2 {
    margin: 0;
    font-weight: 400;
    font-size: 27px;
    line-height: 34px;
    color: var(--heading-white);
  }
  .statement .rule {
    height: 0;
    border-top: 2px dotted var(--rule-yellow);
    margin: 2px 0 8px;
  }
  .statement p {
    margin: 0;
    font-size: 19px;
    line-height: 31px;
    color: var(--body-text);
  }
  .statement--vision { top: 822px; }
  .statement--mission { top: 953px; }
  .statement--objective { top: 1057px; }
</style>
</head>
<body>
<main class="page">
  <svg class="backdrop" width="919" height="1200" viewBox="0 0 919 1200" xmlns="http://www.w3.org/2000/svg">
    <defs>
      <linearGradient id="photoTone" x1="0" y1="0" x2="0.4" y2="1">
        <stop offset="0" stop-color="var(--photo-light)"/>
        <stop offset="0.45" stop-color="#b9a99a"/>
        <stop offset="1" stop-color="var(--photo-dark)"/>
      </linearGradient>
      <radialGradient id="greenField" cx="0.72" cy="0.05" r="1" fx="0.72" fy="0.05">
        <stop offset="0" stop-color="var(--green-light)"/>
        <stop offset="0.45" stop-color="var(--green-mid)"/>
        <stop offset="1" stop-color="var(--green-dark)"/>
      </radialGradient>
    </defs>
    <path class="portrait" role="img" aria-label="Portrait photograph of a businessman in glasses, suit and tie" d="M0,0 L400,0 L400,535 C470,560 560,610 650,690 L650,800 L0,800 Z" fill="url(#photoTone)"/>
    <path class="band-silver" d="M0,752 C260,748 500,618 919,498 L919,530 C500,648 260,778 0,782 Z" fill="var(--band-silver)"/>
    <path class="band-blue" d="M0,762 C260,758 500,630 919,508 L919,534 C500,654 260,782 0,784 Z" fill="var(--band-blue)"/>
    <path class="green-field" d="M0,776 C260,774 500,650 919,528 L919,1200 L0,1200 Z" fill="url(#greenField)"/>
  </svg>

  <h1 class="page-title">Vision, Mission &amp;<br>Objective</h1>

  <section class="statement statement--vision">
    <h2>Vision</h2>
    <div class="rule"></div>
    <p>To become a benchmark software solution provider in IT industry based on ethics,<br>relationship and expertise</p>
  </section>

  <section class="statement statement--mission">
    <h2>Mission</h2>
    <div class="rule"></div>
    <p>To provide a qualitative solution through balancing triple constraints- Scope, Time and Cost.</p>
  </section>

  <section class="statement statement--objective">
    <h2>Objective</h2>
    <div class="rule"></div>
    <p>To support our customer to overcome their business challenge and achieve the goal with<br>right solution at right time.</p>
  </section>
</main>
</body>
</html>
```